Coastal Rubdown Oil Co. needs a new label.

This massage oil has been in Australia for over 20 years and needs a new label for its plastic 250ml bottles. The current label (8cm x 8cm) looks old fashioned and so we are looking for something that reflects freedom, relaxation, inspiration. The product is made from sweet almond oil and has different essential oils used to give unique smells. I have seen some lovely abstract vector images. I think we need a clean straight look with bright colours. There are currently six variations to the product. "Weary and Worn Heads, Achy and Spent Frames, Couples Mix, Heather Soak Oil, Unwinding Mix, Uplift Mix" Different coloured labels have been used for each of the blends. I have included photos of existing bottles plus some ideas for the labels.

I would like to use the same font on the name of the brand Bramblewick Acres. If we change the font it may be difficult for existing customers to find our product.

Also just under the name Bramblewick Acres I would like to insert a type of logo (can be the shape of a tear drop or round circle) to say:

Massage Oil
Since 1970

The size of the label is 8cm x 12 cm for the front and the same size for the back of the label.
Updates

Coastal Rubdown oil Company has posted on the brief some images from Pixelvault plus two photos of the original bottles. I am looking for a new design which is bright in colour, fun and funky. I am not thinking along the lines of the traditional Herb and trees look. I think the original label is too busy and the colours overpower the label. The other point I think that is important is that the product has been around since 1970. If there is room I think a round logo which says: Massage Oil Since 1970 I am hoping that we can fit this information on the label Looking forward to seeing all the designs come thru. So far I have only had two designs come thru. Speak soon from hot sunny Australia. maree

Thank you to everyone who has already posted designs for our Massage Label. I have now edited the brief to include some more ideas on how to make this design the Best! I will email back to you straight away ideas and thoughts on your designs. Remember I live in Australia and can be either 10hrs in front or behind your time.

Reason: Due to busy lives and commitments over the next few days I feel that an extension will benefit all involved. Thank you to everyone who has submitted designs and working with me to create something beautiful. maree

Hello from Australia all the designers who have submitted some wonderful designs over the past two weeks. We are now entering the final three days of the competition. Thank you to everyone who has worked so hard to try and create the perfect label for my massage oil bottle. All of you have done a fantastic job. This has made the decision hard to make. Thank you to everyone. Please submit all your last minute designs soon. kind regards maree Australia

Target Market(s)

The type of person purchasing a massage oil blend will buy from a health food shop, pharmacy or from an on-line store. I believe they are wanting something bright that clearly communicates that that it is a massage oil.

Industry/Entity Type

Massage

Font styles to use
Script

Requirements
Must have
• Different colour for each massage oil blend.
Need same font for the name Bramblewick Acres. (script font or similar)

Abstract design please.
Nice to have
• A logo under the name Bramblewick Acres

Tear Drop or circle design that says:

Massage Oil
Since 1970

also we would like an outline for the back label. (see photo attached)

BACK LABEL information

A unique blend of essential oils in a fine light base.

Contains:

vegetable oil extract of nettle, sweet almond oil, ethanol, essential oils of lavender, lemongrass, orange & ylang ylang and vitamin E.

How to Use:

Shake well warm bottle in warm water if very cold.
Lovingly massage the body from head to toe.
Not for medicinal use.

Bramblewick Acres
Hollin WA 6099
Phone: (08) 9555 0142

(LEAVE ROOM FOR BARCODE)
Should not have
• Too busy design or old fashioned design.
No dull colours.

```html
<!DOCTYPE html>
<html lang="en">
<head>
<meta charset="utf-8">
<title>Bramblewick Acres – Weary &amp; Worn Heads Massage Oil Label</title>
<link href="https://fonts.googleapis.com/css2?family=Great+Vibes&family=Marcellus&family=Marcellus+SC&family=EB+Garamond:wght@400;500&family=PT+Sans:wght@400;700&display=swap" rel="stylesheet">
<style>
  :root{
    --page:#ffffff;
    --sky:#bfe1f1;
    --panel:#b9dcef;
    --navy:#1a5fb0;
    --ink:#1f63ad;
    --pattern-light:#cbe6f3;
    --pattern-mid:#8cc7df;
    --pattern-deep:#5aa3d0;
    --white:#ffffff;
  }
  *{box-sizing:border-box;margin:0;padding:0}
  html,body{width:1200px;height:900px;overflow:hidden;background:var(--page)}
  .canvas{position:relative;width:1200px;height:900px;background:var(--page)}

  .label{position:absolute;top:74px;width:474px;height:708px;overflow:hidden}
  .label--front{left:114px}
  .label--back{left:614px;width:476px}

  .pattern-fill{
    position:absolute;left:0;right:0;bottom:0;
    background:linear-gradient(160deg,var(--pattern-light) 0%,var(--pattern-mid) 45%,var(--pattern-light) 70%,var(--pattern-deep) 100%);
  }
  .label--front .pattern-fill{top:220px}
  .label--back .pattern-fill{top:0}

  .brand-band{position:absolute;left:0;top:0;width:100%;height:220px;background:var(--sky);text-align:center;color:var(--ink)}
  .brand-name{font-family:'Great Vibes',cursive;font-size:60px;line-height:1;padding-top:50px;color:var(--ink)}
  .brand-dot{display:block;width:14px;height:14px;border-radius:50%;background:var(--navy);margin:8px auto 6px}
  .product-type{font-family:'Marcellus',serif;font-size:31px;letter-spacing:0.5px;line-height:1}
  .since{font-family:'PT Sans',sans-serif;font-weight:700;font-size:11px;letter-spacing:0.5px;margin-top:4px}

  .name-plate{position:absolute;display:flex;align-items:center;justify-content:center}
  .name-plate svg{position:absolute;inset:0;width:100%;height:100%}
  .name-plate__text{position:relative;font-family:'Marcellus SC',serif;color:var(--white);white-space:nowrap}
  .label--front .name-plate{left:46px;top:378px;width:386px;height:86px}
  .label--front .name-plate__text{font-size:33px}
  .label--back .name-plate{left:76px;top:40px;width:322px;height:72px}
  .label--back .name-plate__text{font-size:27px}

  .volume{position:absolute;left:0;width:100%;top:622px;text-align:center;font-family:'EB Garamond',serif;font-size:24px;color:var(--ink)}

  .info-panel{position:absolute;left:102px;top:150px;width:272px;height:482px;background:var(--panel);border:4px solid var(--white);border-radius:26px;box-shadow:inset 0 0 0 4px var(--panel),inset 0 0 0 5px var(--ink)}
  .info{position:absolute;left:0;top:0;width:100%;padding:64px 20px 0;font-family:'EB Garamond',serif;color:var(--ink);font-size:15.5px;line-height:19px;text-align:center}
  .info p{margin-bottom:19px}
  .info .heading{margin-bottom:0}
  .info .usage{text-align:left}
  .info .ingredients{margin-bottom:52px}

  .contact{position:absolute;left:50px;top:382px;font-family:'PT Sans',sans-serif;font-size:12px;line-height:16px;color:var(--ink);display:flex;gap:8px}
  .contact__dot{width:10px;height:10px;border-radius:50%;background:var(--navy);margin-top:3px;flex:none}
  .contact__name{text-transform:uppercase}
</style>
</head>
<body>
<main class="canvas">

  <section class="label label--front" aria-label="Front label">
    <div class="pattern-fill" role="img" aria-label="Abstract blue and aqua leaf pattern background"></div>
    <header class="brand-band">
      <h1 class="brand-name">Bramblewick Acres</h1>
      <span class="brand-dot"></span>
      <p class="product-type">MASSAGE OIL</p>
      <p class="since">SINCE 1970</p>
    </header>
    <div class="name-plate">
      <svg viewBox="0 0 386 86" preserveAspectRatio="none" aria-hidden="true">
        <path d="M14 0 H372 A14 14 0 0 0 386 14 V72 A14 14 0 0 0 372 86 H14 A14 14 0 0 0 0 72 V14 A14 14 0 0 0 14 0 Z" fill="#1a5fb0"/>
        <path d="M18 6 H368 A12 12 0 0 0 380 18 V68 A12 12 0 0 0 368 80 H18 A12 12 0 0 0 6 68 V18 A12 12 0 0 0 18 6 Z" fill="none" stroke="#ffffff" stroke-width="1.5"/>
      </svg>
      <span class="name-plate__text">Weary &amp; Worn Heads</span>
    </div>
    <p class="volume">250 ml</p>
  </section>

  <section class="label label--back" aria-label="Back label">
    <div class="pattern-fill" role="img" aria-label="Abstract blue and aqua leaf pattern background"></div>
    <div class="name-plate">
      <svg viewBox="0 0 322 72" preserveAspectRatio="none" aria-hidden="true">
        <path d="M12 0 H310 A12 12 0 0 0 322 12 V60 A12 12 0 0 0 310 72 H12 A12 12 0 0 0 0 60 V12 A12 12 0 0 0 12 0 Z" fill="#1a5fb0"/>
        <path d="M16 5 H306 A11 11 0 0 0 317 16 V56 A11 11 0 0 0 306 67 H16 A11 11 0 0 0 5 56 V16 A11 11 0 0 0 16 5 Z" fill="none" stroke="#ffffff" stroke-width="1.5"/>
      </svg>
      <span class="name-plate__text">Weary &amp; Worn Heads</span>
    </div>

    <div class="info-panel">
      <div class="info">
        <p>A unique blend of essential<br>oils in a fine light base.</p>
        <p class="heading">CONTAINS:</p>
        <p class="ingredients">Vegetable oil extract of nettle, sweet almond oil, ethanol, essential oils of lavender, lemongrass, orange and yland-ylang and Vitamin E.</p>
        <p class="heading">HOW TO USE:</p>
        <p class="usage">Shake well.&nbsp; Warm bottle in warm water is very cold.&nbsp; Lovingly massage the body from head to toe.&nbsp; Not for medicinal use.</p>
      </div>
      <address class="contact">
        <span class="contact__dot"></span>
        <span><span class="contact__name">Bramblewick Acres</span><br>Hollin, WA 6099<br>Phone: (08) 9555 0142</span>
      </address>
    </div>
  </section>

</main>
</body>
</html>
```